Business card - Home housekeeping/concierge

*** This project is connected to our other Business Logo project but Sketch Hive have created two separate links...

Please look at both links and if you are interested submit your designs for both the logo and business card projects.

http://briefs.sketchhive.example/brief.aspx?id=402918
AND
http://briefs.sketchhive.example/brief.aspx?id=402966
***

We are launching a new business in the coming weeks - Tidyhaven Keepers is the business name. Services include: domestic cleaning, ironing, dog walking, special events

We are after bright and happy blues - orange - yellow - green - some silver/grey. The logo is being designed at the same time as part of this project.

Please enter both the logo and business card competition as we will be using the winning logo design for the business card.
Updates

I have created a business card project AND a logo project and even though they are for the same business Sketch Hive has given me two links. Please look at both links and if you are interested submit your designs for both the logo and business card projects. Apologies for my newbie mistakes learning how to use Sketch Hive. I have asked for a logo and a business card and have two links: http://briefs.sketchhive.example/brief.aspx?id=402918 AND http://briefs.sketchhive.example/brief.aspx?id=402966

*** This project is linked to a Business card design project - Sketch Hive have given me two separate links... http://briefs.sketchhive.example/brief.aspx?id=402918 AND http://briefs.sketchhive.example/brief.aspx?id=402966

Target Market(s)

Busy professionals, retired/elderly, families wanting regular cleaning and one-off end of rental lease cleans (so also real estate property managers, home owners and renters).

Industry/Entity Type

Business

Font styles to use
Sans Serif

Colors
0255a3
f37123
ffc213
00a990

Requirements
Must have
• Business name - Tidyhaven Keepers
Nice to have
• Something representing a home, cleaning equipment (eg a broom, mop, iron and ironing board, socks and underwear hanging on a line).

```html
<!DOCTYPE html>
<html lang="en">
<head>
<meta charset="utf-8">
<title>Tidyhaven Keepers – Business Card</title>
<link rel="stylesheet" href="https://fonts.googleapis.com/css2?family=Open+Sans:wght@400;600;700&display=swap">
<style>
  :root {
    --backdrop: #e6e6e6;
    --card: #f7f7f5;
    --ink: #1f1f1f;
    --red: #e8332a;
    --blue: #2a8fd6;
    --navy: #2f3c9e;
    --skin: #f4c4a0;
    --hair: #1c1c22;
  }
  * { box-sizing: border-box; margin: 0; padding: 0; }
  html, body {
    width: 1200px;
    height: 873px;
    overflow: hidden;
  }
  body {
    background: var(--backdrop);
    font-family: "Open Sans", Arial, sans-serif;
    position: relative;
  }
  .card {
    position: absolute;
    top: 273px;
    width: 540px;
    height: 327px;
    background: var(--card);
    box-shadow: 0 6px 18px rgba(0,0,0,0.18);
    overflow: hidden;
  }
  .card--front { left: 40px; }
  .card--back { left: 620px; }

  /* Front */
  .front__details {
    position: absolute;
    left: 30px;
    top: 26px;
    color: var(--ink);
  }
  .business-name {
    font-size: 27px;
    font-weight: 400;
    letter-spacing: 0.2px;
    line-height: 1.1;
  }
  .business-name .word-a { color: var(--red); }
  .business-name .word-b { color: var(--blue); }
  .person-name {
    margin-top: 12px;
    font-size: 22px;
    line-height: 1.1;
  }
  .person-role {
    font-size: 14px;
    color: var(--blue);
    margin-bottom: 8px;
  }
  .address {
    font-size: 14px;
    line-height: 1.4;
    font-style: normal;
  }
  .contact {
    margin-top: 2px;
    font-size: 14px;
    line-height: 1.4;
  }
  .contact .label-phone { color: var(--red); }
  .contact .label-email { color: var(--blue); }
  .front__illustration {
    position: absolute;
    right: 20px;
    bottom: 0;
    width: 200px;
    height: 250px;
    border-radius: 100px 100px 0 0;
    background: linear-gradient(180deg, var(--hair) 0%, var(--skin) 35%, var(--navy) 60%, var(--red) 100%);
    opacity: 0.85;
  }

  /* Back */
  .back__illustration {
    position: absolute;
    border-radius: 14px;
    opacity: 0.85;
  }
  .back__illustration--top {
    left: 150px;
    top: 18px;
    width: 260px;
    height: 88px;
    background: linear-gradient(90deg, var(--navy) 0%, #c9c9cf 55%, var(--blue) 100%);
  }
  .back__illustration--right {
    left: 360px;
    top: 150px;
    width: 155px;
    height: 150px;
    background: linear-gradient(180deg, #d47a3c 0%, var(--skin) 35%, var(--navy) 100%);
  }
  .logo {
    position: absolute;
    left: 28px;
    top: 116px;
    display: flex;
    align-items: flex-start;
    gap: 12px;
  }
  .logo__dot {
    flex: none;
    width: 20px;
    height: 20px;
    margin-top: 22px;
    border-radius: 50%;
    background: var(--red);
  }
  .logo__name {
    font-size: 52px;
    font-weight: 700;
    color: var(--navy);
    line-height: 1.08;
    letter-spacing: 0.5px;
  }
  .logo__name span { display: block; }
</style>
</head>
<body>

  <section class="card card--front">
    <div class="front__details">
      <h1 class="business-name"><span class="word-a">Tidyhaven</span> <span class="word-b">Keepers</span></h1>
      <p class="person-name">Marla Penrose</p>
      <p class="person-role">Director</p>
      <address class="address">
        PO Box 518<br>
        Seabrook<br>
        Qld 4290<br>
        Australia
      </address>
      <p class="contact"><span class="label-phone">Phone</span> 0400 555 137</p>
      <p class="contact"><span class="label-email">Email</span> hello@tidyhavenkeepers.example</p>
    </div>
    <div class="front__illustration" role="img" aria-label="Illustration of a housekeeper in a blue top and polka-dot headscarf holding a feather duster"></div>
  </section>

  <section class="card card--back">
    <div class="back__illustration back__illustration--top" role="img" aria-label="Illustration of a housekeeper with a feather duster beside a clothesline of chores: a list, a broom and a dog"></div>
    <div class="back__illustration back__illustration--right" role="img" aria-label="Illustration of a red-haired housekeeper in a blue top beside a hanging shirt"></div>
    <div class="logo">
      <span class="logo__dot"></span>
      <p class="logo__name"><span>Tidyhaven</span><span>Keepers</span></p>
    </div>
  </section>

</body>
</html>
```